Modern business card design for professional copywriter

I'd like a business card design that I can use to have my cards printed out by plink.com as a squared corners business card (see artwork and design guidelines here: https://help.plink.com/hc/en-gb/sections/300481726-PLINK-Product-Templates)

The design should be clean and modern and reflect the colours, tone and branding on my website: https://noravestrel.com.au

Target Market(s)

Professionals, B2B small business owners

Industry/Entity Type

Business

Contact Information for Business Card

Nora Vestrel
m: 0427 593 864
e: nora@noravestrel.com.au
w: noravestrel.com.au

Font styles to use
Sans Serif

Requirements
Must have
• Tagline: "Smart copywriting for clever business people"
• Brand colours: fd8000, 009984, 666666 and black
Nice to have

```html
<!DOCTYPE html>
<html lang="en">
<head>
<meta charset="utf-8">
<title>Nora Vestrel — Business Card</title>
<link href="https://fonts.googleapis.com/css2?family=Questrial&family=Arimo:wght@400;700&family=Open+Sans:wght@400;600&display=swap" rel="stylesheet">
<style>
  :root {
    --brand-orange: #fd8000;
    --brand-orange-deep: #e87400;
    --brand-orange-shade: #a85400;
    --brand-teal: #009984;
    --brand-grey: #666666;
    --brand-black: #0b0b0b;
    --paper: #ffffff;
    --paper-soft: #ececec;
    --stage: #d9d9d9;
  }
  * { margin: 0; padding: 0; box-sizing: border-box; }
  html, body {
    width: 1200px;
    height: 997px;
    overflow: hidden;
    background: var(--stage);
  }
  .sheet {
    position: relative;
    width: 1200px;
    height: 997px;
  }
  .card {
    position: absolute;
    width: 640px;
    height: 366px;
    border-radius: 18px;
    overflow: hidden;
    left: 280px;
  }

  /* Front */
  .card-front {
    top: 92px;
    background: linear-gradient(160deg, #f58a22 0%, var(--brand-orange-deep) 100%);
  }
  .card-front .brand-block {
    position: absolute;
    left: 120px;
    top: 118px;
  }
  .card-front .brand-name {
    font-family: "Questrial", sans-serif;
    font-size: 56px;
    line-height: 1;
    color: var(--paper);
    letter-spacing: 0.5px;
  }
  .card-front .brand-descriptor {
    font-family: "Questrial", sans-serif;
    font-size: 15px;
    letter-spacing: 6px;
    color: #b85e00;
    text-align: right;
    margin-top: 6px;
  }
  .card-front .tagline {
    font-family: "Open Sans", sans-serif;
    font-size: 19px;
    color: var(--paper);
    margin-top: 14px;
  }

  /* Back */
  .card-back {
    top: 538px;
    background: var(--paper);
  }
  .card-back .card-shapes {
    position: absolute;
    inset: 0;
  }
  .card-back .brand-block {
    position: absolute;
    left: 120px;
    top: 62px;
  }
  .card-back .brand-name {
    font-family: "Questrial", sans-serif;
    font-size: 50px;
    line-height: 1;
    color: var(--brand-teal);
    letter-spacing: 0.5px;
  }
  .card-back .brand-descriptor {
    font-family: "Questrial", sans-serif;
    font-size: 15px;
    letter-spacing: 6px;
    color: var(--brand-grey);
    text-align: right;
    margin-top: 4px;
  }
  .holder {
    position: absolute;
    left: 150px;
    width: 350px;
    top: 176px;
    text-align: center;
  }
  .holder-name {
    font-family: "Arimo", sans-serif;
    font-weight: 700;
    font-size: 18px;
    letter-spacing: 1px;
    color: var(--paper);
  }
  .holder-role {
    font-family: "Arimo", sans-serif;
    font-size: 14px;
    color: var(--brand-black);
    margin-top: 2px;
  }
  .website {
    position: absolute;
    right: 34px;
    top: 258px;
    font-family: "Arimo", sans-serif;
    font-weight: 700;
    font-size: 17px;
    letter-spacing: 0.5px;
    color: var(--brand-orange);
    text-transform: uppercase;
  }
  .contact-list {
    position: absolute;
    left: 30px;
    top: 296px;
    list-style: none;
  }
  .contact-item {
    display: flex;
    align-items: center;
    gap: 14px;
    height: 26px;
    font-family: "Arimo", sans-serif;
    font-size: 16px;
    color: #e6e6e6;
  }
  .contact-icon {
    width: 20px;
    height: 20px;
    flex: none;
  }
</style>
</head>
<body>
<main class="sheet">

  <section class="card card-front" aria-label="Business card front">
    <div class="brand-block">
      <div class="brand-name">Nora Vestrel</div>
      <div class="brand-descriptor">COPYWRITER</div>
      <p class="tagline">Smart copywriting for clever business people</p>
    </div>
  </section>

  <section class="card card-back" aria-label="Business card back">
    <svg class="card-shapes" width="640" height="366" viewBox="0 0 640 366" aria-hidden="true">
      <defs>
        <linearGradient id="paperFade" x1="0" y1="0" x2="0" y2="1">
          <stop offset="0" stop-color="#ffffff"/>
          <stop offset="1" stop-color="#e9e9e9"/>
        </linearGradient>
      </defs>
      <rect width="640" height="200" fill="url(#paperFade)"/>
      <rect y="200" width="640" height="166" fill="#0b0b0b"/>
      <rect y="194" width="640" height="6" fill="#fd8000"/>
      <polygon points="118,196 150,168 500,168 532,196" fill="#a85400"/>
      <polygon points="150,168 500,168 522,196 500,232 150,232 128,196" fill="#f07a00"/>
      <polygon points="128,196 150,232 150,200" fill="#a85400"/>
      <polygon points="522,196 500,232 500,200" fill="#a85400"/>
    </svg>

    <div class="brand-block">
      <div class="brand-name">Nora Vestrel</div>
      <div class="brand-descriptor">COPYWRITER</div>
    </div>

    <div class="holder">
      <div class="holder-name">NORA VESTREL</div>
      <div class="holder-role">Copy Writer</div>
    </div>

    <div class="website">www.noravestrel.com.au</div>

    <ul class="contact-list">
      <li class="contact-item">
        <svg class="contact-icon" viewBox="0 0 20 20" aria-label="Phone">
          <circle cx="10" cy="10" r="10" fill="#fd8000"/>
          <path d="M6 7.5c0-1 1.8-1.8 4-1.8s4 .8 4 1.8l-1.3.6-.6-1H7.9l-.6 1z M6.5 13.5l1.5-4h4l1.5 4z" fill="#ffffff"/>
        </svg>
        <span>0427 593 864</span>
      </li>
      <li class="contact-item">
        <svg class="contact-icon" viewBox="0 0 20 20" aria-label="Email">
          <circle cx="10" cy="10" r="10" fill="#fd8000"/>
          <rect x="5" y="6.5" width="10" height="7" fill="#ffffff"/>
          <path d="M5 6.5l5 4 5-4" fill="none" stroke="#fd8000" stroke-width="1"/>
        </svg>
        <span>nora@noravestrel.com.au</span>
      </li>
    </ul>
  </section>

</main>
</body>
</html>
```